Business Card Design for Cybersecurity Company - Quorvent Systems

We need a business card design for our new cybersecurity company, Quorvent. We’re going for a clean, hi tech look that feels modern, premium, and trustworthy. We want a design that really stands out and makes people say WOW when we hand it over!

Quorvent delivers reliable IT support and managed services for small and mid sized businesses. We help companies stay secure, efficient, and connected through proactive monitoring, cybersecurity services, cloud management, and remote support.

Target Market(s)

Designers should target small and mid sized businesses that need dependable cybersecurity and IT support.

Industry/Entity Type

Cybersecurity, Managed Service Provider, IT services

Contact Information for Business Card

Contact information

Requirements
Must have
• The card should look clean, modern, and tech focused, with the Quorvent logo, clear contact info, and strong readability. It needs to feel premium and professional while still keeping a simple layout that fits a cybersecurity and IT brand.
Nice to have
• Nice to have elements include subtle touches that give the card a modern, tech feel, along with a layout that works well in different background styles.
Should not have
• The card should avoid clutter, loud graphics, or anything that takes attention away from the logo and contact details.

```html
<!DOCTYPE html>
<html lang="en">
<head>
<meta charset="utf-8">
<title>Quorvent Systems – Business Card</title>
<link rel="stylesheet" href="https://fonts.googleapis.com/css2?family=Raleway:wght@400;500;600&display=swap">
<style>
  :root {
    --backdrop: #bababa;
    --paper: #ffffff;
    --violet: #6a2ee0;
    --blue: #2f7cf6;
    --brand: #4a52e8;
    --ink: #1d1d1f;
    --muted: #5a5a60;
    --rule: #7fa6f0;
  }
  * { box-sizing: border-box; margin: 0; padding: 0; }
  html, body { width: 1200px; height: 802px; overflow: hidden; }
  body {
    background: var(--backdrop);
    font-family: "Raleway", Arial, sans-serif;
    display: flex;
    align-items: center;
    justify-content: center;
    gap: 30px;
  }
  .card {
    position: relative;
    width: 560px;
    height: 320px;
    border-radius: 10px;
    overflow: hidden;
  }
  /* Front */
  .card-front { background: var(--paper); color: var(--ink); }
  .brand {
    position: absolute;
    left: 24px;
    top: 22px;
    display: flex;
    align-items: center;
    gap: 12px;
  }
  .brand-mark {
    width: 58px; height: 58px;
    border-radius: 50%;
    background: var(--brand);
  }
  .brand-name {
    font-size: 27px;
    font-weight: 600;
    color: var(--brand);
    letter-spacing: 0.3px;
  }
  .person {
    position: absolute;
    right: 22px;
    top: 150px;
    text-align: right;
  }
  .person-name {
    font-size: 29px;
    font-weight: 500;
    color: var(--blue);
    line-height: 1.1;
  }
  .person-role {
    margin-top: 8px;
    font-size: 15px;
    color: var(--muted);
  }
  .divider {
    position: absolute;
    left: 22px; right: 22px;
    top: 221px;
    height: 1px;
    background: var(--rule);
  }
  .contacts {
    position: absolute;
    left: 22px;
    top: 235px;
    list-style: none;
    font-size: 14.5px;
    line-height: 22px;
  }
  .contacts li { display: flex; align-items: center; gap: 7px; }
  .contacts svg { width: 13px; height: 13px; fill: var(--brand); flex: none; }
  .web-pill {
    position: absolute;
    right: 0;
    top: 264px;
    height: 32px;
    padding: 0 18px 0 12px;
    border-radius: 16px 0 0 16px;
    background: linear-gradient(90deg, var(--blue), var(--violet));
    color: #fff;
    font-size: 14.5px;
    display: flex;
    align-items: center;
    gap: 7px;
  }
  .web-pill svg { width: 14px; height: 14px; fill: none; stroke: #fff; stroke-width: 1.6; }
  /* Back */
  .card-back {
    background: linear-gradient(90deg, var(--violet), var(--blue));
    display: flex;
    align-items: center;
    justify-content: center;
    gap: 16px;
  }
  .card-back .brand-mark { width: 86px; height: 86px; background: #fff; }
  .card-back .brand-name { color: #fff; font-size: 38px; }
</style>
</head>
<body>
  <section class="card card-front" aria-label="Card front">
    <div class="brand">
      <span class="brand-mark"></span>
      <span class="brand-name">Quorvent Systems</span>
    </div>
    <div class="person">
      <h1 class="person-name">Dana Mercer</h1>
      <p class="person-role">Owner | CEO | Quorvent Systems</p>
    </div>
    <div class="divider"></div>
    <ul class="contacts">
      <li><svg viewBox="0 0 16 16"><path d="M2 6c0-2 3-3 6-3s6 1 6 3v1h-3V5.5H5V7H2z M4 8h8l1 6H3z"/></svg>(555) 214 0188</li>
      <li><svg viewBox="0 0 16 16"><path d="M4 1l3 3-2 2c1 2 3 4 5 5l2-2 3 3-2 3C7 15 1 9 1 3z"/></svg>(555) 390-2716</li>
      <li><svg viewBox="0 0 16 16"><path d="M15 1L1 7l6 2 2 6z"/></svg>dana@quorventsys.com</li>
    </ul>
    <div class="web-pill">
      <svg viewBox="0 0 16 16"><circle cx="8" cy="8" r="6.5"/><path d="M1.5 8h13M8 1.5c-3 3.5-3 9.5 0 13M8 1.5c3 3.5 3 9.5 0 13"/></svg>
      www.quorventsys.com
    </div>
  </section>

  <section class="card card-back" aria-label="Card back">
    <span class="brand-mark"></span>
    <span class="brand-name">Quorvent Systems</span>
  </section>
</body>
</html>
```